design a construction company business card

Design business card around our logo. Card must have all the typical info: name, title, address, phone, email, business name, etc. Somewhere on the card I would like to see our motto "Grounded in Trust... Driven by Dedication." Consider adding a splash of bright orange to the card to complement the blues and silvers/grays in the logo. We are open to metallic inks, textures, etc. We would like to see options on both light and dark backgrounds. The font in the logo is Euro Technic Extended Regular.

```html
<!DOCTYPE html>
<html lang="en">
<head>
<meta charset="utf-8">
<title>Halden Contracting, Inc. – Business Card</title>
<link href="https://fonts.googleapis.com/css2?family=Aleo:wght@400;600;700&display=swap" rel="stylesheet">
<style>
  :root {
    --page: #f6f6f6;
    --card: #232122;
    --blue: #1f76c8;
    --blue-deep: #2a3f9e;
    --grey: #8a8a8c;
    --white: #ffffff;
  }
  * { margin: 0; padding: 0; box-sizing: border-box; }
  html, body { width: 1200px; height: 754px; overflow: hidden; }
  body { background: var(--page); font-family: "Aleo", Georgia, serif; position: relative; }

  .card {
    position: absolute; top: 226px; width: 529px; height: 302px;
    background: var(--card);
    box-shadow: 0 10px 22px rgba(0,0,0,.28);
    overflow: hidden;
  }
  .card--front { left: 50px; }
  .card--back { left: 621px; width: 528px; }

  /* front */
  .brand { position: absolute; left: 30px; top: 170px; color: var(--blue); font-weight: 600; line-height: 1; }
  .brand__name { font-size: 52px; letter-spacing: 4px; }
  .brand__sub { font-size: 16px; letter-spacing: 2px; margin-top: 10px; margin-left: 4px; }
  .motto { position: absolute; left: 32px; top: 254px; color: var(--grey); font-size: 14.5px; white-space: nowrap; }
  .base-line { position: absolute; height: 7px; background: linear-gradient(90deg, var(--blue-deep), var(--blue)); }
  .card--front .base-line { left: 25px; top: 276px; width: 310px; }
  .skyline { position: absolute; }
  .card--front .skyline { left: 340px; top: 17px; width: 162px; height: 267px;
    background: linear-gradient(90deg, var(--blue-deep) 0%, #5f6067 45%, var(--blue) 100%); }

  /* back */
  .address { position: absolute; left: 26px; top: 52px; color: var(--blue); font-size: 13.5px; line-height: 21px; }
  .brand--small { left: auto; right: 27px; top: 60px; text-align: right; }
  .brand--small .brand__name { font-size: 30px; letter-spacing: 2px; }
  .brand--small .brand__sub { font-size: 10px; letter-spacing: 1.5px; margin-top: 5px; margin-left: 0; }
  .card--back .skyline { left: 26px; top: 132px; width: 78px; height: 152px;
    background: linear-gradient(90deg, #6f7074 0%, #6f7074 14%, var(--card) 14%, var(--card) 42%, var(--blue) 42%, var(--blue-deep) 100%); }
  .card--back .base-line { left: 104px; top: 276px; width: 424px; }
  .contacts { position: absolute; left: 114px; top: 169px; list-style: none; color: var(--white); font-size: 13.5px; }
  .contacts li { display: flex; align-items: center; height: 21.3px; }
  .contacts svg { width: 14px; height: 14px; margin-right: 7px; fill: var(--blue); flex: none; }
  .person { position: absolute; right: 27px; top: 168px; text-align: right; }
  .person__name { color: var(--blue); font-size: 20px; font-weight: 700; line-height: 24px; }
  .person__title { color: var(--white); font-size: 12px; }
  .tab { position: absolute; right: 0; top: 172px; width: 11px; height: 32px; background: var(--blue); }
</style>
</head>
<body>
  <section class="card card--front">
    <div class="skyline" role="img" aria-label="Decorative rising building bars in blue and grey"></div>
    <div class="brand">
      <div class="brand__name">HALDEN</div>
      <div class="brand__sub">CONTRACTING, INC.</div>
    </div>
    <p class="motto">Grounded in Trust... Driven by Dedication</p>
    <div class="base-line"></div>
  </section>

  <section class="card card--back">
    <p class="address">318/4 Keel St, Riverton<br>NSW 2071, NY</p>
    <div class="brand brand--small">
      <div class="brand__name">HALDEN</div>
      <div class="brand__sub">CONTRACTING, INC.</div>
    </div>
    <div class="skyline" role="img" aria-label="Decorative building bars in grey and blue"></div>
    <div class="base-line"></div>
    <ul class="contacts">
      <li><svg viewBox="0 0 24 24"><path d="M6.6 10.8a15.1 15.1 0 0 0 6.6 6.6l2.2-2.2a1 1 0 0 1 1-.25 11.4 11.4 0 0 0 3.6.57 1 1 0 0 1 1 1V20a1 1 0 0 1-1 1A17 17 0 0 1 3 4a1 1 0 0 1 1-1h3.5a1 1 0 0 1 1 1c0 1.250.2 2.450.57 3.570a1 1 0 0 1-.25 1z"/></svg>(02) 5550 1842</li>
      <li><svg viewBox="0 0 24 24"><path d="M7 1h10a2 2 0 0 1 2 2v18a2 2 0 0 1-2 2H7a2 2 0 0 1-2-2V3a2 2 0 0 1 2-2zm0 3v14h10V4zm5 15.2a1.1 1.1 0 1 0 0 2.2 1.1 1.1 0 0 0 0-2.2z"/></svg>0400 555 217</li>
      <li><svg viewBox="0 0 24 24"><path d="M2 5h20v2l-10 6L2 7zm0 4.3 10 6 10-6V19H2z"/></svg>info@haldencontracting.com</li>
      <li><svg viewBox="0 0 24 24"><path d="M12 2a10 10 0 1 0 0 20 10 10 0 0 0 0-20zm-1 17.9A8 8 0 0 1 4.1 10L9 15v1a2 2 0 0 0 2 2zm6.9-2.5A2 2 0 0 0 16 16h-1v-3a1 1 0 0 0-1-1H8v-2h2a1 1 0 0 0 1-1V7h2a2 2 0 0 0 2-2v-.4a8 8 0 0 1 2.9 12.8z"/></svg>www.haldencontracting.com</li>
    </ul>
    <div class="person">
      <div class="person__name">Marcus Reed</div>
      <div class="person__title">Founder | CEO</div>
    </div>
    <div class="tab"></div>
  </section>
</body>
</html>
```